Design few pages for professional development app

I need a website design for a prototype project. The goal of the project is to prototype a few basic screens for a professional development application.

The final design should be clean, modern, and appeal to a professional millenial clientele.The designs have been wireframed (see attached), and we'd like these wireframes converted to design files.

Here is the list of goals and tasks that correspond to the design: https://sheets.plorvane.com/tables/d/7qWmK84x9PLzn3oTcB2vEaRyhUDs-kfNJ52tqXyMHw/edit?usp=sharing

Number of Pages Required

5+ page

Font styles to use
Serif
Sans Serif

Colors

Designer to choose colors to be used in the design.

Requirements
Nice to have
• Uses Google Material Design, Bootstrap, or another framework

```html
<!DOCTYPE html>
<html lang="en">
<head>
<meta charset="utf-8">
<title>ClimbPath — Take Control of Your Career</title>
<link href="https://fonts.googleapis.com/css2?family=Barlow:wght@400;500;600;700&display=swap" rel="stylesheet">
<style>
:root{
  --ink:#1f2326;
  --muted:#555c61;
  --teal:#26aebd;
  --teal-deep:#1e8a94;
  --hero-dark:#07262b;
  --hero-mid:#0f4a52;
  --lavender:#cfd9fb;
  --aqua-pale:#e3f6f9;
  --paper:#ffffff;
  --grey-bg:#f2f2f2;
  --footer:#2a2a2a;
  --line:#c9ced2;
}
*{box-sizing:border-box;margin:0;padding:0}
html,body{width:1200px;height:4060px;overflow:hidden}
body{font-family:'Barlow',sans-serif;color:var(--ink);background:var(--paper);position:relative}
section,header,footer{position:relative;width:1200px}
.abs{position:absolute}
.card{position:absolute;background:var(--paper);box-shadow:0 2px 6px rgba(0,0,0,.14)}
.pill{position:absolute;display:flex;align-items:center;border-radius:30px;background:var(--teal);color:#fff;font-weight:600;text-transform:uppercase;box-shadow:0 3px 6px rgba(0,0,0,.15)}
.pill .dot{width:38px;height:38px;border-radius:50%;background:#fff;display:flex;align-items:center;justify-content:center;margin:0 12px 0 4px}
.badge{width:48px;height:48px;border-radius:50%;background:var(--teal);display:flex;align-items:center;justify-content:center}

/* Hero */
.hero{height:615px;overflow:hidden}
.hero-art{position:absolute;inset:0;background:radial-gradient(circle at 78% 55%,#1f6f78 0%,#124950 28%,var(--hero-dark) 70%),var(--hero-dark)}
.brand{left:128px;top:40px;font-size:40px;font-weight:600;color:#fff;letter-spacing:-.5px}
.nav-icons{right:128px;top:58px;display:flex;gap:14px}
.hero h1{left:128px;top:168px;font-size:48px;line-height:60px;color:#fff;font-weight:400}
.hero h1 strong{display:block;font-weight:700}
.hero p{left:128px;top:298px;width:480px;font-size:21px;line-height:32px;color:#fff}
.hero .pill{left:128px;top:452px;height:46px;width:203px;font-size:18px}

/* Testimonials */
.praise{height:297px;background:var(--lavender)}
.quote{top:65px;width:448px;height:143px;display:flex;align-items:center;padding:0 26px}
.avatar{width:82px;height:82px;border-radius:50%;flex:none;background:linear-gradient(160deg,#c9d3d8,#6e7f88);border:3px solid var(--teal);margin-right:18px}
.quote p{font-size:18px;line-height:27px;color:#333}
.quote cite{display:block;font-style:normal;font-size:14px;color:#444;margin-top:8px}

/* Sign up */
.signup{height:610px;overflow:hidden}
.signup-art{position:absolute;inset:0;background:radial-gradient(circle at 10% 80%,#2a9aa4,transparent 45%),radial-gradient(circle at 92% 25%,#2a9aa4,transparent 40%),var(--teal-deep)}
.signup .card{left:285px;top:78px;width:595px;height:437px;box-shadow:0 4px 14px rgba(0,0,0,.2)}
.signup h2{position:absolute;top:38px;width:100%;text-align:center;font-size:31px;font-weight:600}
.field{position:absolute;left:54px;width:486px;height:37px;border:1px solid var(--line);font-size:12px;color:#555;padding:10px 12px}
.field.focus{border-color:#555}
.agree{position:absolute;left:54px;top:314px;font-size:12px;display:flex;align-items:center;gap:10px}
.box{width:12px;height:12px;border:1.5px solid #333;display:inline-block}
.btn{position:absolute;top:350px;height:39px;font-size:13px;font-weight:600;color:#fff;display:flex;align-items:center;justify-content:center;text-transform:uppercase}
.btn.dark{left:54px;width:126px;background:var(--ink)}
.btn.light{left:199px;width:126px;background:var(--teal)}

/* Goals */
.goals{height:604px;background:var(--aqua-pale)}
.section-title{position:absolute;width:100%;text-align:center;font-size:38px;font-weight:600}
.section-sub{position:absolute;width:100%;text-align:center;font-size:23px;color:#333}
.goal{width:448px;height:79px;display:flex;align-items:center;padding-left:25px;font-size:19px}
.tick{width:16px;height:16px;background:var(--ink);border-radius:2px;display:flex;align-items:center;justify-content:center;margin-right:38px}
.goal .badge{margin-right:24px}
.goals .pill{left:464px;top:449px;width:272px;height:47px;justify-content:center;font-size:19px;text-transform:none}

/* Tasks */
.tasks{height:847px;background:var(--lavender)}
.task{width:290px;height:251px;text-align:center}
.task .badge{position:absolute;left:121px;top:24px}
.task h3{position:absolute;top:88px;width:100%;font-size:20px;font-weight:500;text-transform:uppercase}
.task p{position:absolute;top:122px;left:30px;right:30px;font-size:15px;line-height:24px;color:#444}
.task .pill{top:184px;height:37px;font-size:16px;padding-right:22px}
.task .pill .dot{width:29px;height:29px;margin:0 12px 0 5px}

/* Learn */
.learn{height:970px;background:var(--grey-bg)}
.author{left:132px;top:179px;width:448px;height:79px;display:flex;align-items:center;padding-left:25px;font-size:18px;line-height:26px}
.author .badge{margin-right:22px}
.learn .pill{left:705px;top:198px;width:361px;height:46px;justify-content:center;font-size:18px;text-transform:none}
.article{left:134px;top:293px;width:934px;height:344px}
.article p{position:absolute;left:25px;top:30px;width:410px;font-size:14px;line-height:30.5px;color:#333}
.video{position:absolute;left:486px;top:27px;width:429px;height:288px;background:radial-gradient(circle at 55% 60%,#1e6a72,#0b3138 70%)}
.notes{left:134px;top:671px;width:934px;height:201px;padding:30px 24px}
.notes h4{font-size:19px;font-weight:500;margin-bottom:16px}
.notes li{list-style:none;font-size:15px;line-height:32px;color:#333}

footer{height:117px;background:var(--footer);color:#fff;font-size:16px;display:flex;align-items:center;justify-content:center}
</style>
</head>
<body>

<header class="hero">
  <div class="hero-art" role="img" aria-label="Dark teal abstract background of flowing contour lines"></div>
  <div class="abs brand">ClimbPath</div>
  <nav class="abs nav-icons" aria-label="Site">
    <svg width="26" height="26" viewBox="0 0 26 26"><rect x="3" y="5" width="20" height="3" fill="#fff"/><rect x="3" y="11.5" width="20" height="3" fill="#fff"/><rect x="3" y="18" width="20" height="3" fill="#fff"/></svg>
    <svg width="26" height="26" viewBox="0 0 26 26"><circle cx="11" cy="11" r="7" fill="none" stroke="#fff" stroke-width="3"/><line x1="16" y1="16" x2="23" y2="23" stroke="#fff" stroke-width="3.5"/></svg>
    <svg width="26" height="26" viewBox="0 0 26 26"><path d="M8 12V8a5 5 0 0 1 10 0" fill="none" stroke="#fff" stroke-width="3"/><rect x="4" y="12" width="18" height="13" rx="1.5" fill="#fff"/><rect x="12" y="16" width="2" height="5" fill="#0f4a52"/></svg>
  </nav>
  <h1 class="abs">TAKE CONTROL<strong>OF YOUR CAREER</strong></h1>
  <p class="abs">Complete short, actionable tasks guaranteed to get you further in your career, faster than ever. Ready to get started? Take the short quiz below and get your personalized path today.</p>
  <div class="pill"><span class="dot"><svg width="20" height="20" viewBox="0 0 20 20"><path d="M10 2v10M5 8l5 5 5-5" fill="none" stroke="#26aebd" stroke-width="2.5"/><rect x="3" y="15" width="14" height="3" fill="#26aebd"/></svg></span>Get Started</div>
</header>

<section class="praise">
  <div class="card quote" style="left:132px">
    <div class="avatar" role="img" aria-label="Portrait photo of Nora Ellis"></div>
    <p>I love how quickly I can do the tasks, and see progress.<cite>— Nora Ellis</cite></p>
  </div>
  <div class="card quote" style="left:612px">
    <div class="avatar" role="img" aria-label="Portrait photo of Theo Marsh"></div>
    <p>The best investment I've made in myself in ages.<cite>— Theo Marsh</cite></p>
  </div>
</section>

<section class="signup">
  <div class="signup-art" role="img" aria-label="Teal background with faint contour line pattern"></div>
  <form class="card">
    <h2>Sign Up To See &amp; Save Your Goals</h2>
    <div class="field focus" style="top:102px">Name:</div>
    <div class="field" style="top:150px">Email:</div>
    <div class="field" style="top:198px">Password:</div>
    <div class="field" style="top:248px">Re-type password:</div>
    <div class="agree"><span class="box"></span>I agree to the Terms of Use and Privacy Policy.</div>
    <div class="btn dark">Sign Up</div>
    <div class="btn light">Learn More</div>
  </form>
</section>

<section class="goals">
  <h2 class="section-title" style="top:75px">What Are Your Main Goals?</h2>
  <p class="section-sub" style="top:132px">Tell us what you would like to achieve with ClimbPath</p>
  <div class="card goal" style="left:132px;top:208px"><span class="tick"><svg width="11" height="9"><path d="M1 4.5l3 3 6-6" fill="none" stroke="#fff" stroke-width="2"/></svg></span><span class="badge"><svg width="30" height="22" viewBox="0 0 30 22"><circle cx="15" cy="6" r="4.5" fill="#fff"/><circle cx="6" cy="8" r="3.2" fill="#fff"/><circle cx="24" cy="8" r="3.2" fill="#fff"/><path d="M8 21a7 7 0 0 1 14 0z" fill="#fff"/><path d="M0 20a6 6 0 0 1 9-5M30 20a6 6 0 0 0-9-5" fill="#fff"/></svg></span>Build my network</div>
  <div class="card goal" style="left:612px;top:208px"><span class="tick"><svg width="11" height="9"><path d="M1 4.5l3 3 6-6" fill="none" stroke="#fff" stroke-width="2"/></svg></span><span class="badge"><svg width="30" height="22" viewBox="0 0 30 22"><circle cx="15" cy="6" r="4.5" fill="#fff"/><circle cx="6" cy="8" r="3.2" fill="#fff"/><circle cx="24" cy="8" r="3.2" fill="#fff"/><path d="M8 21a7 7 0 0 1 14 0z" fill="#fff"/><path d="M0 20a6 6 0 0 1 9-5M30 20a6 6 0 0 0-9-5" fill="#fff"/></svg></span>Personal branding</div>
  <div class="card goal" style="left:132px;top:312px"><span class="tick"><svg width="11" height="9"><path d="M1 4.5l3 3 6-6" fill="none" stroke="#fff" stroke-width="2"/></svg></span><span class="badge"><svg width="30" height="22" viewBox="0 0 30 22"><circle cx="15" cy="6" r="4.5" fill="#fff"/><circle cx="6" cy="8" r="3.2" fill="#fff"/><circle cx="24" cy="8" r="3.2" fill="#fff"/><path d="M8 21a7 7 0 0 1 14 0z" fill="#fff"/><path d="M0 20a6 6 0 0 1 9-5M30 20a6 6 0 0 0-9-5" fill="#fff"/></svg></span>Get a promotion</div>
  <div class="card goal" style="left:612px;top:312px"><span class="tick"><svg width="11" height="9"><path d="M1 4.5l3 3 6-6" fill="none" stroke="#fff" stroke-width="2"/></svg></span><span class="badge"><svg width="30" height="22" viewBox="0 0 30 22"><circle cx="15" cy="6" r="4.5" fill="#fff"/><circle cx="6" cy="8" r="3.2" fill="#fff"/><circle cx="24" cy="8" r="3.2" fill="#fff"/><path d="M8 21a7 7 0 0 1 14 0z" fill="#fff"/><path d="M0 20a6 6 0 0 1 9-5M30 20a6 6 0 0 0-9-5" fill="#fff"/></svg></span>Be a bettter leader</div>
  <div class="pill">See My Personalized List</div>
</section>

<section class="tasks">
  <h2 class="section-title" style="top:70px">Nora, here's your list of suggested tasks</h2>
  <p class="section-sub" style="top:129px">Tell us what you would like to achieve with ClimbPath</p>

  <article class="card task" style="left:129px;top:210px">
    <span class="abs badge"><svg width="30" height="22" viewBox="0 0 30 22"><circle cx="15" cy="6" r="4.5" fill="#fff"/><circle cx="6" cy="8" r="3.2" fill="#fff"/><circle cx="24" cy="8" r="3.2" fill="#fff"/><path d="M8 21a7 7 0 0 1 14 0z" fill="#fff"/><path d="M0 20a6 6 0 0 1 9-5M30 20a6 6 0 0 0-9-5" fill="#fff"/></svg></span>
    <h3>Personal Branding</h3><p>Write Your Personal Brand Statement</p>
    <div class="pill" style="left:59px"><span class="dot"><svg width="16" height="16"><rect width="16" height="16" rx="2" fill="#26aebd"/><path d="M3.5 8l3 3 6-6" fill="none" stroke="#fff" stroke-width="2"/></svg></span>Completed</div>
  </article>
  <article class="card task" style="left:454px;top:210px">
    <span class="abs badge"><svg width="26" height="24" viewBox="0 0 26 24"><path d="M2 9h5l12-7v20L7 15H2z" fill="#fff"/><path d="M6 15l3 8h3l-2-8z" fill="#fff"/><path d="M22 8a4 4 0 0 1 0 8" fill="none" stroke="#fff" stroke-width="2"/></svg></span>
    <h3>Get a Promotion</h3><p>Have A Career Conversation With Your Manager</p>
    <div class="pill" style="left:64px"><span class="dot"><svg width="16" height="16"><circle cx="8" cy="8" r="8" fill="#26aebd"/><path d="M6 4.5v7l6-3.5z" fill="#fff"/></svg></span>Start Task</div>
  </article>
  <article class="card task" style="left:777px;top:210px">
    <span class="abs badge"><svg width="26" height="24" viewBox="0 0 26 24"><path d="M2 9h5l12-7v20L7 15H2z" fill="#fff"/><path d="M6 15l3 8h3l-2-8z" fill="#fff"/><path d="M22 8a4 4 0 0 1 0 8" fill="none" stroke="#fff" stroke-width="2"/></svg></span>
    <h3>Get a Promotion</h3><p>Ask 4 Peers For Candid Feedback</p>
    <div class="pill" style="left:64px"><span class="dot"><svg width="16" height="16"><circle cx="8" cy="8" r="8" fill="#26aebd"/><path d="M6 4.5v7l6-3.5z" fill="#fff"/></svg></span>Start Task</div>
  </article>

  <article class="card task" style="left:129px;top:498px">
    <span class="abs badge"><svg width="30" height="22" viewBox="0 0 30 22"><circle cx="15" cy="6" r="4.5" fill="#fff"/><circle cx="6" cy="8" r="3.2" fill="#fff"/><circle cx="24" cy="8" r="3.2" fill="#fff"/><path d="M8 21a7 7 0 0 1 14 0z" fill="#fff"/><path d="M0 20a6 6 0 0 1 9-5M30 20a6 6 0 0 0-9-5" fill="#fff"/></svg></span>
    <h3>Personal Branding</h3><p>Write Your Personal Brand Statement</p>
    <div class="pill" style="left:88px"><span class="dot"><svg width="16" height="16"><circle cx="8" cy="8" r="8" fill="#26aebd"/><path d="M6 4.5v7l6-3.5z" fill="#fff"/></svg></span>Start</div>
  </article>
  <article class="card task" style="left:454px;top:498px">
    <span class="abs badge"><svg width="26" height="24" viewBox="0 0 26 24"><path d="M2 9h5l12-7v20L7 15H2z" fill="#fff"/><path d="M6 15l3 8h3l-2-8z" fill="#fff"/><path d="M22 8a4 4 0 0 1 0 8" fill="none" stroke="#fff" stroke-width="2"/></svg></span>
    <h3>Get a Promotion</h3><p>Have A Career Conversation With Your Manager</p>
    <div class="pill" style="left:88px"><span class="dot"><svg width="16" height="16"><circle cx="8" cy="8" r="8" fill="#26aebd"/><path d="M6 4.5v7l6-3.5z" fill="#fff"/></svg></span>Start</div>
  </article>
  <article class="card task" style="left:777px;top:498px">
    <span class="abs badge"><svg width="26" height="24" viewBox="0 0 26 24"><path d="M2 9h5l12-7v20L7 15H2z" fill="#fff"/><path d="M6 15l3 8h3l-2-8z" fill="#fff"/><path d="M22 8a4 4 0 0 1 0 8" fill="none" stroke="#fff" stroke-width="2"/></svg></span>
    <h3>Get a Promotion</h3><p>Ask 4 Peers For Candid Feedback</p>
    <div class="pill" style="left:88px"><span class="dot"><svg width="16" height="16"><circle cx="8" cy="8" r="8" fill="#26aebd"/><path d="M6 4.5v7l6-3.5z" fill="#fff"/></svg></span>Start</div>
  </article>
</section>

<section class="learn">
  <h2 class="section-title" style="top:80px">Learn about Career Conversations</h2>
  <div class="card author"><span class="badge"><svg width="30" height="22" viewBox="0 0 30 22"><circle cx="15" cy="6" r="4.5" fill="#fff"/><circle cx="6" cy="8" r="3.2" fill="#fff"/><circle cx="24" cy="8" r="3.2" fill="#fff"/><path d="M8 21a7 7 0 0 1 14 0z" fill="#fff"/><path d="M0 20a6 6 0 0 1 9-5M30 20a6 6 0 0 0-9-5" fill="#fff"/></svg></span><span>By Idris Vale<br>Senior Marketing Leader, Kestrel Group</span></div>
  <div class="pill"><svg width="18" height="18" style="margin-right:10px"><rect width="18" height="18" rx="2" fill="#fff"/><path d="M4 9l3.5 3.5L14 6" fill="none" stroke="#26aebd" stroke-width="2.2"/></svg>Finished this task? Mark Complete</div>
  <div class="card article">
    <p>Lorem ipsum dolor sit amet, consectetur adipiscing elit. Vivamus rhoncus vulputate sollicitudin. Ut commodo gravida orci vel mattis. Mauris vitae elit dui. Donec enim enim, euismod a felis ac, aliquam varius leo. Etiam pretium pharetra leo, vitae scelerisque est egestas convallis. Interdum et malesuada fames ac ante ipsum primis in faucibus. Vivamus vel egestas ex, et molestie enim. Psque nec mollis libero, vel iaculis mauris. Nullam arcu est, ctum vitae ornare ac, blandit in dui.</p>
    <div class="video" role="img" aria-label="Video still with teal contour line pattern">
      <svg class="abs" style="left:190px;top:120px" width="50" height="50" viewBox="0 0 50 50"><circle cx="25" cy="25" r="23" fill="none" stroke="#fff" stroke-width="2"/><path d="M19 14v22l18-11z" fill="none" stroke="#fff" stroke-width="2"/></svg>
    </div>
  </div>
  <div class="card notes">
    <h4>Lorem ipsum dolor sit amet, consectetur adipiscing elit.</h4>
    <ul>
      <li>+ Vivamus rhoncus vulputate sollicitudin.</li>
      <li>+ Ut commodo gravida orci vel mattis.</li>
      <li>+ Mauris vitae elit dui. Donec enim enim, euismod a felis ac, aliquam varius leo.</li>
    </ul>
  </div>
</section>

<footer>©2019 ClimbPath, All Rights Reserved.</footer>

</body>
</html>
```